Dane Morrow Photography Business Card

I am looking for a simple, yet elegant business card for my photography business.

It is a short turn around project as the cards need to be printed within 48 hours. So the earlier you submit, the more likely you are to be chosen.

I am a professional portrait, sports and commercial photographer located in Brisbane, Australia. I am looking for a professional business card to distribute to professional clients. The card needs to be professional and easy to read. It must have my contact information as listed below.

Industry/Entity Type

Business

Contact Information for Business Card

Dane Morrow Photography
www.danemorrowphoto.com.au
dane@danemorrowphoto.com.au
+61 437 280 556

Font styles to use
Serif
Sans Serif

Colors
ffc214
fece3e
fee18a

Requirements
Must have
• Must have contact information as above,
• Please use a similar colourscheme to the one provided in the logo upload.
Nice to have
• A very simple, design, happy to have some geometric shapes etc. Must look professional

```html
<!DOCTYPE html>
<html lang="en">
<head>
<meta charset="utf-8">
<title>Dane Morrow Photography — Business Card</title>
<link rel="stylesheet" href="https://fonts.googleapis.com/css2?family=Lato:wght@300&family=Roboto:wght@300&family=Roboto+Condensed:wght@700&display=swap">
<style>
  :root {
    --charcoal: #3a3a3c;
    --panel: #e6e7e9;
    --pattern-light: #eceef0;
    --pattern-dark: #dcdee1;
    --gold: #ffc214;
    --mark-gold: #c98a1e;
    --wordmark: #4a4a4c;
    --ink: #111111;
    --text: #1e1e1e;
  }
  * { margin: 0; padding: 0; box-sizing: border-box; }
  html, body { width: 1200px; height: 686px; overflow: hidden; background: var(--panel); }
  .card { position: relative; width: 1200px; height: 686px; background: var(--panel); overflow: hidden; }

  .top-bar { position: absolute; left: 0; top: 0; width: 1200px; height: 38px; background: var(--charcoal); }

  .brand-panel {
    position: absolute; left: 0; top: 38px; width: 1200px; height: 317px;
    background: radial-gradient(ellipse at center, var(--pattern-light) 0%, var(--pattern-dark) 100%);
  }
  .brand-mark {
    position: absolute; left: 252px; top: 95px; width: 186px; height: 186px;
    border-radius: 50%; background: var(--mark-gold);
  }
  .brand-wordmark {
    position: absolute; left: 475px; top: 134px;
    font-family: "Lato", sans-serif; font-weight: 300; color: var(--wordmark);
    text-transform: uppercase; line-height: 1;
  }
  .brand-name { display: block; font-size: 76px; letter-spacing: -1px; }
  .brand-tag { display: block; font-size: 40px; margin-top: 6px; margin-left: 3px; }

  .gold-rule { position: absolute; left: 0; top: 355px; width: 1200px; height: 10px; background: var(--gold); }

  .business-title {
    position: absolute; left: 0; top: 390px; width: 1200px; text-align: center; line-height: 1;
  }
  .title-name {
    display: block; font-family: "Roboto Condensed", sans-serif; font-weight: 700;
    font-size: 62px; color: var(--ink); margin-left: -14px;
  }
  .title-tag {
    display: block; font-family: "Roboto", sans-serif; font-weight: 300;
    font-size: 42px; color: var(--ink); margin-top: 0; margin-left: -14px;
  }

  .contact {
    position: absolute; display: flex; align-items: center;
    font-family: "Roboto", sans-serif; font-weight: 300; font-size: 33px; color: var(--text);
    line-height: 1;
  }
  .contact svg { flex: none; fill: var(--charcoal); }
  .contact-phone { left: 416px; top: 520px; }
  .contact-phone svg { margin-right: 28px; }
  .contact-email { left: 45px; top: 589px; }
  .contact-email svg { margin-right: 18px; }
  .contact-web { left: 635px; top: 589px; }
  .contact-web svg { margin-right: 24px; }

  .bottom-band { position: absolute; left: 0; top: 660px; width: 1200px; height: 26px; background: var(--gold); }
</style>
</head>
<body>
<main class="card">
  <div class="top-bar"></div>

  <section class="brand-panel" role="img" aria-label="Subtle grey geometric diamond pattern background">
  </section>
  <div class="brand-mark" aria-hidden="true"></div>
  <div class="brand-wordmark">
    <span class="brand-name">Dane Morrow</span>
    <span class="brand-tag">Photography</span>
  </div>

  <div class="gold-rule"></div>

  <h1 class="business-title">
    <span class="title-name">DANE MORROW</span>
    <span class="title-tag">PHOTOGRAPHY</span>
  </h1>

  <p class="contact contact-phone">
    <svg width="32" height="32" viewBox="0 0 24 24" aria-hidden="true"><path d="M6.6 10.8c1.4 2.8 3.8 5.1 6.6 6.6l2.2-2.2c.3-.3.7-.4 1-.2 1.1.4 2.3.6 3.6.6.6 0 1 .4 1 1V20c0 .6-.4 1-1 1C10.6 21 3 13.4 3 4c0-.6.4-1 1-1h3.5c.6 0 1 .4 1 1 0 1.3.2 2.5.6 3.6.1.3 0 .7-.2 1L6.6 10.8z"/></svg>
    <span>+61 437 280 556</span>
  </p>

  <p class="contact contact-email">
    <svg width="30" height="20" viewBox="0 0 30 20" aria-hidden="true"><path d="M0 0h30v20H0z M2 3v15h26V3L15 12z M3 2l12 8 12-8z" fill-rule="evenodd"/></svg>
    <span>dane@danemorrowphoto.com.au</span>
  </p>

  <p class="contact contact-web">
    <svg width="30" height="30" viewBox="0 0 30 30" aria-hidden="true"><circle cx="15" cy="15" r="14"/><path d="M3 15h24M15 2c-4 4-4 22 0 26M15 2c4 4 4 22 0 26" stroke="#e6e7e9" stroke-width="1.6" fill="none"/></svg>
    <span>www.danemorrowphoto.com.au</span>
  </p>

  <div class="bottom-band"></div>
</main>
</body>
</html>
```